Core Investment Strategy's Super Pie Chart

We need a one page visual explanation of an investment strategy we call "Core/Perimeter". This strategy emphasizes a "core" portfolio that will seldom change and "perimeter" investments that will change. Our investment management firm caters to wealthy individuals. We want to project an image of strength and reliability. At the same time, we are willing to explore new concepts. I have uploaded a PDF of my graphically-challenged assistant's attempt at creating the one page visual.

Industry/Entity Type

Investment

```html
<!DOCTYPE html>
<html lang="en">
<head>
<meta charset="utf-8">
<title>Core/Perimeter Portfolio</title>
<link rel="stylesheet" href="https://fonts.googleapis.com/css2?family=Carlito:wght@400;700&display=swap">
<style>
  :root {
    --bg-center: #ffffff;
    --bg-edge: #d6d8db;
    --title-fill: #4f81bd;
    --title-text: #ffffff;
    --label-text: #2b2b2b;
    --alt-assets: #1f3a5f;
    --alt-assets-side: #142844;
    --funds: #d40d12;
    --funds-side: #9b0a0d;
    --core-assets: #507c2a;
    --core-assets-side: #3a5c1d;
    --other: #9656b4;
    --large-cap: #0f6ccb;
    --large-cap-side: #0a4f96;
    --mid-cap: #1d8de8;
    --mid-cap-side: #156bb2;
    --small-cap: #3ea8f3;
    --small-cap-side: #2d83c0;
    --intl-equities: #1cc2f6;
    --intl-equities-side: #1494bd;
    --short-bonds: #8fd13f;
    --short-bonds-side: #6aa02c;
    --inter-bonds: #6fad35;
  }
  * { margin: 0; padding: 0; box-sizing: border-box; }
  html, body { width: 1200px; height: 908px; overflow: hidden; }
  body {
    position: relative;
    font-family: "Carlito", "Calibri", sans-serif;
    background: radial-gradient(ellipse at 50% 45%, var(--bg-center) 0%, #f1f2f3 45%, var(--bg-edge) 100%);
    color: var(--label-text);
  }
  .slide-title {
    position: absolute;
    left: 374px; top: 84px;
    width: 443px; height: 73px;
    background: var(--title-fill);
    color: var(--title-text);
    font-size: 27px;
    font-weight: 700;
    display: flex; align-items: center; justify-content: center;
    letter-spacing: -0.3px;
  }
  .portfolio-chart { position: absolute; left: 0; top: 0; }
  .ring-label {
    position: absolute;
    font-size: 15.5px;
    line-height: 1.4;
    white-space: nowrap;
  }
  .ring-label.other { left: 241px; top: 298px; }
  .ring-label.alternative { left: 855px; top: 298px; }
  .ring-label.funds { left: 875px; top: 514px; }
  .ring-label.core { right: 893px; top: 494px; text-align: right; }
  .legend {
    position: absolute;
    left: 0; width: 1200px;
    font-size: 13px;
  }
  .legend-row {
    position: absolute;
    display: flex; gap: 12px;
    white-space: nowrap;
  }
  .legend-row.first { left: 369px; top: 795px; }
  .legend-row.second { left: 366px; top: 823px; }
  .legend-item { display: flex; align-items: center; gap: 4px; }
  .swatch { width: 8px; height: 8px; display: inline-block; }
</style>
</head>
<body>
  <div class="slide-title">Core/Perimeter Portfolio</div>

  <svg class="portfolio-chart" width="1200" height="908" viewBox="0 0 1200 908" role="img" aria-label="Core/Perimeter portfolio pie chart">
    <defs>
      <radialGradient id="sheen" cx="45%" cy="35%" r="70%">
        <stop offset="0%" stop-color="#ffffff" stop-opacity="0.28"/>
        <stop offset="60%" stop-color="#ffffff" stop-opacity="0.05"/>
        <stop offset="100%" stop-color="#000000" stop-opacity="0.12"/>
      </radialGradient>
    </defs>

    <!-- perimeter ring: sides -->
    <g class="perimeter-sides">
      <path d="M342,460 L342,505 A260,213 0 0 0 602,718 L602,673 A260,213 0 0 1 342,460 Z" fill="var(--core-assets-side)"/>
      <path d="M602,673 L602,718 A260,213 0 0 0 862,505 L862,460 A260,213 0 0 1 602,673 Z" fill="var(--funds-side)"/>
    </g>

    <!-- perimeter ring: top face -->
    <g class="perimeter-top">
      <path d="M602,460 L602,247 A260,213 0 0 1 862,460 Z" fill="var(--alt-assets)"/>
      <path d="M602,460 L862,460 A260,213 0 0 1 602,673 Z" fill="var(--funds)"/>
      <path d="M602,460 L602,673 A260,213 0 0 1 342,460 Z" fill="var(--core-assets)"/>
      <path d="M602,460 L342,460 A260,213 0 0 1 602,247 Z" fill="var(--other)"/>
      <ellipse cx="602" cy="460" rx="260" ry="213" fill="url(#sheen)"/>
    </g>

    <!-- core pie: shadow and sides -->
    <ellipse cx="600" cy="430" rx="188" ry="158" fill="#000" opacity="0.18"/>
    <g class="core-sides">
      <path d="M780,403 L780,423 A184,160 0 0 1 714.3,545.6 L714.3,525.6 A184,160 0 0 0 780,403 Z" fill="var(--large-cap-side)"/>
      <path d="M714.3,525.6 L714.3,545.6 A184,160 0 0 1 652.9,575.2 L652.9,555.2 A184,160 0 0 0 714.3,525.6 Z" fill="var(--mid-cap-side)"/>
      <path d="M652.9,555.2 L652.9,575.2 A184,160 0 0 1 596,583 L596,563 A184,160 0 0 0 652.9,555.2 Z" fill="var(--small-cap-side)"/>
      <path d="M596,563 L596,583 A184,160 0 0 1 429.2,490.6 L429.2,470.6 A184,160 0 0 0 596,563 Z" fill="var(--intl-equities-side)"/>
      <path d="M429.2,470.6 L429.2,490.6 A184,160 0 0 1 412,423 L412,403 A184,160 0 0 0 429.2,470.6 Z" fill="var(--short-bonds-side)"/>
    </g>

    <!-- core pie: top face -->
    <g class="core-top">
      <path d="M596,403 L596,243 A184,160 0 0 1 714.3,525.6 Z" fill="var(--large-cap)"/>
      <path d="M596,403 L714.3,525.6 A184,160 0 0 1 652.9,555.2 Z" fill="var(--mid-cap)"/>
      <path d="M596,403 L652.9,555.2 A184,160 0 0 1 596,563 Z" fill="var(--small-cap)"/>
      <path d="M596,403 L596,563 A184,160 0 0 1 429.2,470.6 Z" fill="var(--intl-equities)"/>
      <path d="M596,403 L429.2,470.6 A184,160 0 0 1 455.1,300.2 Z" fill="var(--short-bonds)"/>
      <path d="M596,403 L455.1,300.2 A184,160 0 0 1 596,243 Z" fill="var(--inter-bonds)"/>
      <ellipse cx="596" cy="403" rx="184" ry="160" fill="url(#sheen)"/>
    </g>
  </svg>

  <div class="ring-label other">Other, 2%</div>
  <div class="ring-label alternative">Alternative Assets, 7%</div>
  <div class="ring-label funds">Funds, 8%</div>
  <div class="ring-label core">Attractive Core<br>Assets, 3%</div>

  <div class="legend">
    <div class="legend-row first">
      <span class="legend-item"><span class="swatch" style="background:var(--inter-bonds)"></span>Intermediate Bonds, 20%</span>
      <span class="legend-item"><span class="swatch" style="background:var(--short-bonds)"></span>Short-Term Bonds, 10%</span>
      <span class="legend-item"><span class="swatch" style="background:var(--large-cap)"></span>Lg. Cap Equities, 30%</span>
    </div>
    <div class="legend-row second">
      <span class="legend-item"><span class="swatch" style="background:var(--mid-cap)"></span>Mid Cap Equities, 5%</span>
      <span class="legend-item"><span class="swatch" style="background:var(--small-cap)"></span>Sm. Cap Equities, 5%</span>
      <span class="legend-item"><span class="swatch" style="background:var(--intl-equities)"></span>Int'l/Dev. Equities, 10%</span>
    </div>
  </div>
</body>
</html>
```